Property Service business needs a cool business card

Looking for an eloquent and unique business card using the logo and colours attached as uploaded files.

Target Market(s)

Body corporates, real estate agents, building managers

Industry/Entity Type

Business

Contact Information for Business Card

- Quorvel Logo
- Construction * Maintenance * Remedial

- Tom Wexley
- Business Manager

- Ph 0417586204
- P.O Box 461 South Melbourne Vic 3090
- Email tom@quorvel.com
- Website www.quorvelpropertyservices.com.au

Requirements
Must have
• Clean and fresh look, colours must be vibrant!
Nice to have
• unique features
Should not have
• Should not be overcrowded

```html
<!DOCTYPE html>
<html lang="en">
<head>
<meta charset="utf-8">
<title>Quorvel Property Services – Business Card</title>
<link rel="stylesheet" href="https://fonts.googleapis.com/css2?family=Michroma&family=Noto+Sans:wght@400;700&display=swap">
<style>
  :root {
    --stage: #2c6cc0;
    --navy: #003aa8;
    --royal: #0a45f5;
    --lime: #7fff00;
    --white: #ffffff;
    --ink: #000000;
  }
  html, body {
    margin: 0;
    width: 1200px;
    height: 1000px;
    overflow: hidden;
    background: var(--stage);
  }
  .canvas { display: block; width: 1200px; height: 1000px; }
  .brand-name { font-family: "Michroma", sans-serif; fill: var(--white); }
  .person-name { font-family: "Noto Sans", sans-serif; font-weight: 700; fill: var(--royal); }
  .person-role { font-family: "Noto Sans", sans-serif; font-weight: 400; fill: var(--royal); }
  .services { font-family: "Noto Sans", sans-serif; font-weight: 700; fill: var(--royal); }
  .contact-label { font-family: "Noto Sans", sans-serif; font-weight: 700; fill: var(--ink); }
  .contact-value { font-family: "Noto Sans", sans-serif; font-weight: 400; fill: var(--ink); }
</style>
</head>
<body>
<svg class="canvas" viewBox="0 0 1200 1000" xmlns="http://www.w3.org/2000/svg">
  <!-- Card front -->
  <g class="card-front">
    <rect x="67" y="60" width="739" height="422" fill="var(--navy)"/>
    <polygon points="67,375 806,150 806,482 67,482" fill="var(--royal)"/>
    <rect class="brand-square" x="140" y="200" width="145" height="145" fill="var(--lime)"/>
    <text class="brand-name" x="333" y="290" font-size="66">Quorvel</text>
  </g>

  <!-- Card back -->
  <g class="card-back">
    <rect x="393" y="518" width="739" height="422" fill="var(--white)"/>
    <polygon points="597,518 1132,518 1132,684 665,684" fill="var(--lime)"/>
    <polygon points="393,518 583,518 652,684 527,940 393,940" fill="var(--royal)"/>
    <text class="brand-name" x="511" y="668" font-size="28" text-anchor="middle">Quorvel</text>

    <text class="person-name" x="1106" y="626" font-size="33" text-anchor="end">Tom Wexley</text>
    <text class="person-role" x="1106" y="651" font-size="20" text-anchor="end">Business Manager</text>

    <text class="services" x="1104" y="731" font-size="20" text-anchor="end">Construction  •  Maintenance  •  Remedial</text>

    <g class="contact-list" font-size="16.5">
      <text class="contact-label" x="664" y="797">Phone</text>
      <text class="contact-label" x="748" y="797">:</text>
      <text class="contact-value" x="762" y="797">0417586204</text>

      <text class="contact-label" x="664" y="818">PO Box</text>
      <text class="contact-label" x="748" y="818">:</text>
      <text class="contact-value" x="762" y="818">461 South Melbourne Vic 3090</text>

      <text class="contact-label" x="664" y="839">E-mail</text>
      <text class="contact-label" x="748" y="839">:</text>
      <text class="contact-value" x="762" y="839">tom@quorvel.com</text>

      <text class="contact-label" x="664" y="860">Website</text>
      <text class="contact-label" x="748" y="860">:</text>
      <text class="contact-value" x="762" y="860">www.quorvelpropertyservices.com.au</text>
    </g>
  </g>
</svg>
</body>
</html>
```